Brantley Studios photography and video creator

I need a business card for my production company. I shoot photography and videography for real estate, adventure sports and businesses

Contact Information for Business Card

simple not to busy

Colors

Designer to choose colors to be used in the design.

Requirements
Must have
• derek@brantleystudios.ca
• phone -5873304127
• instagram derek_brantley

```html
<!DOCTYPE html>
<html lang="en">
<head>
<meta charset="utf-8">
<title>Brantley Studios – Business Card</title>
<link href="https://fonts.googleapis.com/css2?family=Lato:wght@400;700&display=swap" rel="stylesheet">
<style>
  :root {
    --card-bg: #fbfbfb;
    --ink: #1a1a1a;
    --mark-dark: #2b2b2b;
    --mark-light: #5a5a5a;
    --mark-text: #ffffff;
  }
  html, body {
    margin: 0;
    padding: 0;
    width: 1200px;
    height: 714px;
    overflow: hidden;
    background: var(--card-bg);
  }
  .business-card {
    position: relative;
    width: 1200px;
    height: 714px;
    background: var(--card-bg);
    font-family: "Lato", sans-serif;
    color: var(--ink);
  }
  .brand-mark {
    position: absolute;
    left: 75px;
    top: 119px;
    width: 512px;
    height: 512px;
    border-radius: 50%;
    background: radial-gradient(circle at 50% 30%, var(--mark-light), var(--mark-dark) 70%);
    display: flex;
    align-items: center;
    justify-content: center;
  }
  .brand-name {
    font-family: "Lato", sans-serif;
    font-weight: 700;
    font-size: 40px;
    letter-spacing: 4px;
    text-transform: uppercase;
    color: var(--mark-text);
    margin-top: 150px;
  }
  .contact-list {
    position: absolute;
    left: 680px;
    top: 262px;
    list-style: none;
    margin: 0;
    padding: 0;
  }
  .contact-item {
    display: flex;
    align-items: center;
    height: 70px;
    font-size: 35px;
    font-weight: 400;
  }
  .contact-icon {
    width: 40px;
    height: 40px;
    margin-right: 26px;
    flex: none;
  }
</style>
</head>
<body>
  <main class="business-card">
    <div class="brand-mark">
      <span class="brand-name">Brantley Studios</span>
    </div>

    <ul class="contact-list">
      <li class="contact-item">
        <svg class="contact-icon" viewBox="0 0 40 40" aria-hidden="true">
          <path d="M4 15 Q20 5 36 15 L33 20 L27 18 L26 14 Q20 12 14 14 L13 18 L7 20 Z" fill="var(--ink)"/>
          <path d="M11 22 L15 17 H25 L29 22 V32 H11 Z" fill="var(--ink)"/>
          <circle cx="20" cy="26" r="3" fill="var(--card-bg)"/>
        </svg>
        <span class="contact-phone">5873304127</span>
      </li>
      <li class="contact-item">
        <svg class="contact-icon" viewBox="0 0 40 40" aria-hidden="true">
          <rect x="4" y="9" width="32" height="22" fill="none" stroke="var(--ink)" stroke-width="3"/>
          <path d="M4 9 L20 22 L36 9 M4 31 L16 19 M36 31 L24 19" fill="none" stroke="var(--ink)" stroke-width="3"/>
        </svg>
        <span class="contact-email">derek@brantleystudios.ca</span>
      </li>
      <li class="contact-item">
        <svg class="contact-icon" viewBox="0 0 40 40" aria-hidden="true">
          <rect x="4" y="4" width="32" height="32" rx="6" fill="none" stroke="var(--ink)" stroke-width="3"/>
        </svg>
        <span class="contact-social">derek_brantley</span>
      </li>
    </ul>
  </main>
</body>
</html>
```